Ridgeway Hearth Partners Business Card

Looking for a new business card layout. We are a real estate firm w/ a logo, old design attached. Must keep the same elements on there, just need a fresh look and possible some foil accents. Looking for a simpler design w/ more modern style.

Target Market(s)

Real Estate clients

Industry/Entity Type

Real Estate Agent

Contact Information for Business Card

Font styles to use
Sans Serif

Requirements
Must have
• all elements on current biz card
Nice to have
• modern look, simpler than we have!
Should not have
• no serif fonts

```html
<!DOCTYPE html>
<html lang="en">
<head>
<meta charset="utf-8">
<title>Ridgeway Hearth Partners Business Card</title>
<link href="https://fonts.googleapis.com/css2?family=Poppins:wght@400;500;600&display=swap" rel="stylesheet">
<style>
  :root {
    --stage: #d9d9db;
    --card-black: #050505;
    --card-back: #111112;
    --logo-grey: #8a8a8c;
    --emboss-grey: #3a3a3c;
    --ink-white: #ffffff;
    --edge-red: #e0141e;
    --photo-light: #e4e2de;
    --photo-teal: #39bfc0;
    --photo-hair: #c9ad82;
  }
  * { box-sizing: border-box; margin: 0; padding: 0; }
  html, body { width: 1200px; height: 800px; overflow: hidden; }
  body {
    background: var(--stage);
    font-family: "Poppins", sans-serif;
    display: flex;
    align-items: center;
    justify-content: center;
    gap: 60px;
  }
  .card {
    width: 520px;
    height: 297px;
    box-shadow: 0 3px 0 var(--edge-red), 0 12px 28px rgba(0,0,0,0.22);
    overflow: hidden;
    position: relative;
  }
  .card--front { display: flex; background: var(--card-black); }
  .card__photo {
    width: 42%;
    height: 100%;
    background:
      radial-gradient(ellipse 40% 35% at 52% 42%, var(--photo-hair) 0%, rgba(201,173,130,0) 100%),
      linear-gradient(180deg, var(--photo-light) 0%, var(--photo-light) 62%, var(--photo-teal) 100%);
  }
  .card__info {
    flex: 1;
    padding: 26px 24px 22px 22px;
    display: flex;
    flex-direction: column;
    align-items: flex-end;
    text-align: right;
    color: var(--ink-white);
  }
  .brand-name {
    align-self: flex-start;
    text-align: left;
    font-weight: 600;
    font-size: 19px;
    line-height: 1.1;
    letter-spacing: 0.5px;
    text-transform: uppercase;
    color: var(--logo-grey);
  }
  .agent { margin-top: 22px; }
  .agent__name { font-weight: 600; font-size: 17px; letter-spacing: 0.3px; line-height: 1.1; }
  .agent__title { font-weight: 500; font-size: 9px; letter-spacing: 0.4px; }
  .contact { margin-top: 14px; font-size: 10.5px; line-height: 1.45; }
  .contact__row { display: flex; align-items: center; justify-content: flex-end; gap: 7px; }
  .contact__row svg { width: 10px; height: 10px; flex: none; }
  .contact__spacer { width: 10px; flex: none; }
  .contact__address { margin-bottom: 4px; }
  .card--back {
    background: var(--card-back);
    display: flex;
    align-items: center;
    justify-content: center;
  }
  .brand-name--emboss {
    align-self: center;
    text-align: center;
    font-size: 30px;
    color: var(--emboss-grey);
  }
</style>
</head>
<body>
  <section class="card card--front">
    <div class="card__photo" role="img" aria-label="Portrait photo of the principal broker"></div>
    <div class="card__info">
      <div class="brand-name">Ridgeway Hearth<br>Partners</div>
      <div class="agent">
        <div class="agent__name">DANA WHITFIELD</div>
        <div class="agent__title">PRINCIPAL BROKER</div>
      </div>
      <div class="contact">
        <div class="contact__address">
          <div class="contact__row"><span>318 NW Cedar Ln</span><span class="contact__spacer"></span></div>
          <div class="contact__row"><span>Pine Hollow, OR 97000</span><span class="contact__spacer"></span></div>
        </div>
        <div class="contact__row"><span>555.014.3190</span>
          <svg viewBox="0 0 10 10"><path d="M2 1 L4 1 L4.6 3 L3.6 3.8 Q4.6 5.6 6.2 6.4 L7 5.4 L9 6 L9 8 Q8 9 6.6 8.8 Q2 7.6 1.2 3.2 Q1 2 2 1Z" fill="#fff"/></svg></div>
        <div class="contact__row"><span>555.018.6627</span>
          <svg viewBox="0 0 10 10"><rect x="2.5" y="0.6" width="5" height="8.8" rx="0.8" fill="none" stroke="#fff" stroke-width="1"/><circle cx="5" cy="8" r="0.5" fill="#fff"/></svg></div>
        <div class="contact__row"><span>dana@ridgewayhearth.com</span>
          <svg viewBox="0 0 10 10"><rect x="0.8" y="2" width="8.4" height="6.4" fill="none" stroke="#fff" stroke-width="1"/><path d="M1 2.4 L5 5.6 L9 2.4" fill="none" stroke="#fff" stroke-width="1"/></svg></div>
        <div class="contact__row"><span>Ridgeway-HearthHomes.com</span>
          <svg viewBox="0 0 10 10"><circle cx="5" cy="5" r="4.2" fill="none" stroke="#fff" stroke-width="1"/><ellipse cx="5" cy="5" rx="1.8" ry="4.2" fill="none" stroke="#fff" stroke-width="0.8"/><path d="M0.8 5 H9.2" stroke="#fff" stroke-width="0.8"/></svg></div>
      </div>
    </div>
  </section>

  <section class="card card--back">
    <div class="brand-name brand-name--emboss">Ridgeway Hearth<br>Partners</div>
  </section>
</body>
</html>
```